Web Design Project (Renewable Energy Services Company)

Hello crowd,

We are looking to create a website for a new company. We would like to have the page already coded, if you do not provide the code as well, please indicate so. I am including a very preliminary approximation of the wireframe.

We do not have the logo either the color pallet, however we have in mind couple websites that would be similar tho these.

http://www.brovanta.example/en/

and

http://www.lumidrax.example/

We did an approximated wireframe our our website, not necesarly to decide on the layout but rather to know how many pages will be needed. It would be around 10 pages. We will need a section that will be an e-commerce page to sell products such as engineering instrumentation, software and consumables such as cable and connectors.

Our company will be called TORVO. We will be based in Monterrey, Mexico. Our focused will be the development of renewable energy projects. Similar scope of services than http://www.brovanta.example/en/ but only for wind and solar projects.

We like something minimalistic. Some of the things that the logo might or might not include would be the monterrey famous hill, but not strictly necessary.
http://en.wikinota.example/wiki/Cerro_de_la_Silla

also TORVO (which stands for TOrnados RVOlenta) the name is similar the bird (seagal) or wind turbines and sun...any of these are only suggestions and we are open to receive any proposals.

There must be a
home page
services page (some subsections)
products page (some subsections)
contact page with contact form

and some additional subsections like careers and partnerships.

We are very excited to start hearing about this project.
Updates

Please for the logo, do not restrict your ideas to the ones provided as it has generated too specific logos. Pleae just allow your imagination to flow for a company that develops renewable energy projects.

Target Market(s)

large companies interested in developing renewable energy projects

Industry/Entity Type

E-Commerce

Requirements
Must have
• Minimalistic and unique design.
Nice to have
• contact form to save contacts in a database

Should not have
• We are looking a very minimalistic logo. It should not be an explicit wind turbine a seagal or anything like that. we are looking for abstract, simple and minimalistic image.

```html
<!DOCTYPE html>
<html lang="es">
<head>
<meta charset="utf-8">
<title>TORVO – Proyectos Renovables</title>
<link rel="stylesheet" href="https://fonts.googleapis.com/css2?family=Ropa+Sans&family=PT+Sans:wght@400;700&display=swap">
<style>
:root{
  --header-light:#f3f9e4;
  --header-green:#cfe59a;
  --nav-top:#5a5a5a;
  --nav-bottom:#242424;
  --accent:#f5a300;
  --accent-dark:#e08a00;
  --title-green:#3b5d14;
  --text-grey:#5b5b5b;
  --link-orange:#e68a00;
  --footer-top:#cfe59f;
  --footer-bottom:#a9cf6f;
  --footer-text:#1e2a10;
  --page-bg:#f6f9ee;
}
*{margin:0;padding:0;box-sizing:border-box}
html,body{width:1200px;height:1051px;overflow:hidden}
body{position:relative;background:var(--page-bg);font-family:"PT Sans",sans-serif}

.site-header{position:absolute;left:0;top:0;width:1200px;height:166px;
  background:radial-gradient(circle at 560px 40px,#ffffff 0,rgba(255,255,255,0) 200px),
             radial-gradient(circle at 1100px 30px,#ffffff 0,rgba(255,255,255,0) 180px),
             linear-gradient(180deg,var(--header-green),var(--header-light));}
.brand{position:absolute;left:64px;top:62px;display:flex;align-items:center;gap:22px}
.brand-mark{width:70px;height:70px;border-radius:50%;background:#4f8fb0}
.brand-name{font-family:"PT Sans",sans-serif;font-size:46px;color:#4a4a4a;letter-spacing:2px}

.checkout{position:absolute;left:1010px;top:92px;width:162px;height:30px;border-radius:15px;
  background:linear-gradient(180deg,#ffc400,var(--accent-dark));color:#fff;font-weight:700;
  font-size:16px;line-height:30px;padding-left:46px}
.checkout svg{position:absolute;left:0;top:-4px}

.main-nav{position:absolute;left:0;top:168px;width:1200px;height:58px;
  background:linear-gradient(180deg,var(--nav-top),var(--nav-bottom));}
.main-nav a{position:absolute;top:0;height:58px;line-height:58px;color:#fff;font-size:17px;text-decoration:none}
.main-nav a.active{top:2px;height:54px;line-height:54px;width:135px;text-align:center;
  background:linear-gradient(180deg,#ffc000,var(--accent-dark));border:1px solid #ffd65a}
.search{position:absolute;left:1012px;top:17px;width:156px;height:28px;border-radius:14px;background:#fff;
  color:#999;font-size:13px;line-height:28px;padding-left:22px}
.search svg{position:absolute;right:10px;top:8px}

.page-title{position:absolute;left:20px;top:276px;font-family:"Ropa Sans",sans-serif;font-size:35px;
  color:var(--title-green);font-weight:400;letter-spacing:.5px}

.hero-photo{position:absolute;left:22px;top:339px;width:764px;height:486px;
  background:linear-gradient(180deg,#1d5fa8 0%,#4d8fd0 45%,#a8cdf0 75%,#dceaf7 100%)}
.hero-shadow{position:absolute;left:22px;top:825px;width:764px;height:60px;
  background:linear-gradient(180deg,rgba(0,0,0,.12),rgba(255,255,255,0))}

.service-list{position:absolute;left:822px;top:372px;list-style:none;width:360px}
.service-list li{position:relative;padding-left:31px;font-size:16.5px;line-height:43px;color:var(--text-grey)}
.service-list li svg{position:absolute;left:0;top:15px}
.service-list li.cont{padding-left:31px}
.energy-links{position:absolute;right:38px;top:850px;font-size:15px;color:var(--link-orange)}

.site-footer{position:absolute;left:0;top:900px;width:1200px;height:151px;
  background:linear-gradient(180deg,var(--footer-top),var(--footer-bottom));border-top:2px solid #e4f0c8}
.footer-left,.footer-right{position:absolute;top:40px;font-size:14px;line-height:31px;color:var(--footer-text)}
.footer-left{left:35px}
.footer-right{left:855px}
.mail-icon{position:absolute;left:1070px;top:30px}
</style>
</head>
<body>

<header class="site-header">
  <div class="brand">
    <span class="brand-mark"></span>
    <span class="brand-name">TORVO</span>
  </div>
  <div class="checkout">
    <svg width="40" height="38" viewBox="0 0 40 38"><path d="M4 8h6l5 18h18l4-12H13" fill="none" stroke="#4a3500" stroke-width="3"/><circle cx="17" cy="32" r="3" fill="#4a3500"/><circle cx="30" cy="32" r="3" fill="#4a3500"/><path d="M24 2v12M19 9l5 5 5-5" stroke="#c0392b" stroke-width="3" fill="none"/></svg>
    Check Out &raquo;
  </div>
</header>

<nav class="main-nav">
  <a style="left:34px">Lnicio</a>
  <a style="left:112px">Servicios</a>
  <a class="active" style="left:213px">Productos</a>
  <a style="left:376px">Nuestra E</a>
  <a style="left:490px">specialidad</a>
  <a style="left:630px">Contacto</a>
  <div class="search">Search
    <svg width="13" height="13" viewBox="0 0 13 13"><circle cx="5" cy="5" r="4" fill="none" stroke="#999" stroke-width="1.5"/><path d="M8 8l4 4" stroke="#999" stroke-width="2"/></svg>
  </div>
</nav>

<h1 class="page-title">PROYECTOS RENOVABLESPARA MEXICO Y LATINO AMERICA</h1>

<div class="hero-photo" role="img" aria-label="Paneles solares bajo un cielo azul con sol brillante y nubes"></div>
<div class="hero-shadow"></div>

<ul class="service-list">
  <li><svg width="16" height="16" viewBox="0 0 16 16"><circle cx="8" cy="8" r="8" fill="var(--accent)"/><path d="M4 8l3 3 5-6" stroke="#fff" stroke-width="2" fill="none"/></svg> Energia Eolica</li>
  <li><svg width="16" height="16" viewBox="0 0 16 16"><circle cx="8" cy="8" r="8" fill="var(--accent)"/><path d="M4 8l3 3 5-6" stroke="#fff" stroke-width="2" fill="none"/></svg>Proyectos de Generacion Eolica desde 1MW</li>
  <li class="cont">hasta 200 MV</li>
  <li><svg width="16" height="16" viewBox="0 0 16 16"><circle cx="8" cy="8" r="8" fill="var(--accent)"/><path d="M4 8l3 3 5-6" stroke="#fff" stroke-width="2" fill="none"/></svg>Analisis Detallado de Recurso Eolico</li>
  <li><svg width="16" height="16" viewBox="0 0 16 16"><circle cx="8" cy="8" r="8" fill="var(--accent)"/><path d="M4 8l3 3 5-6" stroke="#fff" stroke-width="2" fill="none"/></svg>Diseno de Parques Eolicos</li>
  <li><svg width="16" height="16" viewBox="0 0 16 16"><circle cx="8" cy="8" r="8" fill="var(--accent)"/><path d="M4 8l3 3 5-6" stroke="#fff" stroke-width="2" fill="none"/></svg>Permitologia</li>
  <li><svg width="16" height="16" viewBox="0 0 16 16"><circle cx="8" cy="8" r="8" fill="var(--accent)"/><path d="M4 8l3 3 5-6" stroke="#fff" stroke-width="2" fill="none"/></svg>Comision Estatal de Redes CER</li>
  <li><svg width="16" height="16" viewBox="0 0 16 16"><circle cx="8" cy="8" r="8" fill="var(--accent)"/><path d="M4 8l3 3 5-6" stroke="#fff" stroke-width="2" fill="none"/></svg>SEMAVERDE</li>
  <li><svg width="16" height="16" viewBox="0 0 16 16"><circle cx="8" cy="8" r="8" fill="var(--accent)"/><path d="M4 8l3 3 5-6" stroke="#fff" stroke-width="2" fill="none"/></svg>RENOVA</li>
  <li><svg width="16" height="16" viewBox="0 0 16 16"><circle cx="8" cy="8" r="8" fill="var(--accent)"/><path d="M4 8l3 3 5-6" stroke="#fff" stroke-width="2" fill="none"/></svg>Analisis de Riesgo y Factibilidad Financiera</li>
  <li><svg width="16" height="16" viewBox="0 0 16 16"><circle cx="8" cy="8" r="8" fill="var(--accent)"/><path d="M4 8l3 3 5-6" stroke="#fff" stroke-width="2" fill="none"/></svg>PPA and Tariff Analysis</li>
</ul>
<div class="energy-links">Energia Eolica &nbsp;|&nbsp; Energia Solar</div>

<footer class="site-footer">
  <div class="footer-left">Carreras | Quienes Somos<br>Copyright © 2012 www.torvo.example</div>
  <div class="footer-right">Alameda 215, Col. Valle Alto<br>Monterrey, N.L. 64890</div>
  <svg class="mail-icon" width="60" height="58" viewBox="0 0 60 58"><g transform="rotate(-15 30 29)"><rect x="6" y="14" width="48" height="32" rx="3" fill="#f7c24a" stroke="#d99a1c"/><path d="M6 16l24 18 24-18" fill="none" stroke="#d99a1c" stroke-width="2"/></g></svg>
</footer>

</body>
</html>
```